Thai Takeaway Menu Design

I need a menu re-design for a thai takeaway/restaurant in australia.

Please use content from the existing menu
http://www.platterwink.example/u/menu/7302918?p=1

I'd like to emphasise on
1 - free delivery for order over $40
2 - gluten free and vegetatian option available on most meal (however you want to word it - not fuss)

*remove (the banner order online and save $10)

I'm happy to change the whole concept & design. I particularly like rustic, raw look more than moden ones. Does not need to be flowery or anything like current one :)

Industry/Entity Type

Restaurant

```html
<!DOCTYPE html>
<html lang="en">
<head>
<meta charset="utf-8">
<title>Thai Takeaway Menu</title>
<link rel="stylesheet" href="https://fonts.googleapis.com/css2?family=Crimson+Text:wght@600;700&display=swap">
<style>
  :root {
    --stage: #e9e9e9;
    --paper-light: #ddd59c;
    --paper-mid: #cdc283;
    --paper-dark: #b3a867;
    --band: #4a3c2b;
    --band-text: #f1ead0;
    --ink: #2f2618;
    --veg-green: #1f9a45;
  }
  * { box-sizing: border-box; margin: 0; padding: 0; }
  html, body { width: 1200px; height: 900px; overflow: hidden; }
  body {
    background: var(--stage);
    font-family: "Crimson Text", "Times New Roman", serif;
    color: var(--ink);
  }
  .menu {
    position: absolute;
    top: 45px; left: 30px;
    width: 1140px; height: 810px;
    display: grid;
    grid-template-columns: repeat(3, 1fr);
    box-shadow: 0 6px 22px rgba(0,0,0,.25);
  }
  .panel {
    position: relative;
    padding: 24px 26px 0;
    background: linear-gradient(160deg, var(--paper-light), var(--paper-mid) 55%, var(--paper-dark));
    border-right: 1px solid rgba(74,60,43,.25);
  }
  .panel:last-child { border-right: none; }
  .section { margin-bottom: 18px; }
  .section-title {
    background: var(--band);
    color: var(--band-text);
    font-weight: 700;
    font-size: 24px;
    line-height: 31px;
    padding: 0 12px;
    margin-bottom: 8px;
  }
  .items { list-style: none; padding: 0 10px; }
  .item {
    display: flex;
    justify-content: space-between;
    font-weight: 700;
    font-size: 15px;
    line-height: 19px;
  }
  .item .price { flex: none; padding-left: 12px; }
  .compact .item { font-size: 14px; line-height: 18px; }
  .compact .section-title { font-size: 22px; line-height: 30px; }

  .footer-band {
    position: absolute;
    left: 0; right: 0; bottom: 22px;
    height: 54px;
    background: var(--band);
    color: var(--band-text);
    display: flex;
    align-items: center;
    justify-content: space-between;
    padding: 0 24px;
    font-weight: 700;
    font-size: 16px;
    line-height: 19px;
  }
  .footer-band .note { text-align: center; flex: 1; }
  .badge {
    flex: none;
    width: 80px; height: 80px;
    border-radius: 50%;
    background: var(--paper-mid);
    border: 3px solid var(--band);
    box-shadow: 0 0 0 4px var(--paper-mid);
    display: flex; align-items: center; justify-content: center;
  }
  .badge-amount {
    font-size: 32px; font-weight: 700; color: var(--band);
  }
  .badge-plain { width: 62px; height: 62px; }
</style>
</head>
<body>
<main class="menu">

  <section class="panel">
    <div class="section">
      <h2 class="section-title">Entrée</h2>
      <ul class="items">
        <li class="item"><span>Spring Rolls*(4)</span><span class="price">$6.00</span></li>
        <li class="item"><span>Satay Chicken(4)</span><span class="price">$6.00</span></li>
        <li class="item"><span>Fish Cakes(4)</span><span class="price">$6.00</span></li>
        <li class="item"><span>Dim Sim (4)</span><span class="price">$6.00</span></li>
        <li class="item"><span>Duck Rice Paper Rolls *(2)</span><span class="price">$6.00</span></li>
        <li class="item"><span>Papaya Salad</span><span class="price">$6.00</span></li>
        <li class="item"><span>Tofu/w Peanut Sauce*</span><span class="price">$6.00</span></li>
      </ul>
    </div>
    <div class="section">
      <h2 class="section-title">Soup</h2>
      <ul class="items">
        <li class="item"><span>Tom Yam Prawn*</span><span class="price">$7.00</span></li>
        <li class="item"><span>Tom kha Chicken *</span><span class="price">$7.00</span></li>
      </ul>
    </div>
    <div class="section">
      <h2 class="section-title">Curry</h2>
      <ul class="items">
        <li class="item"><span>Green Curry Chicken</span><span class="price">$12.90</span></li>
        <li class="item"><span>Panang Chicken</span><span class="price">$12.90</span></li>
        <li class="item"><span>Red Curry Beef</span><span class="price">$12.90</span></li>
        <li class="item"><span>Massaman Beef Curry</span><span class="price">$12.90</span></li>
        <li class="item"><span>Red Duck Curry</span><span class="price">$16.90</span></li>
        <li class="item"><span>Yellow Curry Chicken</span><span class="price">$16.90</span></li>
        <li class="item"><span>Yellow curry Prawn</span><span class="price">$16.90</span></li>
      </ul>
    </div>
    <div class="section">
      <h2 class="section-title">Vegetable</h2>
      <ul class="items">
        <li class="item"><span>Mixed vegetable</span><span class="price">$10.50</span></li>
        <li class="item"><span>Steamed Veg /w Peanut Sauce</span><span class="price">$10.50</span></li>
      </ul>
    </div>
    <div class="section">
      <h2 class="section-title">Beef</h2>
      <ul class="items">
        <li class="item"><span>Beef/w Oyster Sauce</span><span class="price">$12.90</span></li>
        <li class="item"><span>Grilled Beef Salad</span><span class="price">$12.90</span></li>
      </ul>
    </div>
    <div class="footer-band">
      <p class="note">Vegetarian Options Available<br>on Most of the Meals</p>
      <div class="badge badge-veg">
        <svg width="40" height="40" viewBox="0 0 40 40" aria-label="Vegetarian symbol">
          <rect x="3" y="3" width="34" height="34" fill="none" stroke="var(--band)" stroke-width="3"/>
          <circle cx="20" cy="20" r="8" fill="var(--veg-green)"/>
        </svg>
      </div>
    </div>
  </section>

  <section class="panel compact">
    <div class="section">
      <h2 class="section-title">Chicken</h2>
      <ul class="items">
        <li class="item"><span>Laab Chicken</span><span class="price">$12.90</span></li>
        <li class="item"><span>Chicken /w Sweet Basil</span><span class="price">$12.90</span></li>
        <li class="item"><span>Chicken /w Cashew Nuts</span><span class="price">$12.90</span></li>
        <li class="item"><span>Grilled Chicken /w Salad</span><span class="price">$12.90</span></li>
        <li class="item"><span>Southern Style Fried Chicken</span><span class="price">$12.90</span></li>
      </ul>
    </div>
    <div class="section">
      <h2 class="section-title">Pork</h2>
      <ul class="items">
        <li class="item"><span>Sweet &amp;Sour Pork</span><span class="price">$12.90</span></li>
        <li class="item"><span>Garlic Pork</span><span class="price">$12.90</span></li>
        <li class="item"><span>Crispy Pork /w Asian Green</span><span class="price">$12.90</span></li>
      </ul>
    </div>
    <div class="section">
      <h2 class="section-title">Duck</h2>
      <ul class="items">
        <li class="item"><span>Roast Duck /w Vegetable &amp;Gravy</span><span class="price">$16.90</span></li>
        <li class="item"><span>Duck/w sweet Basil</span><span class="price">$16.90</span></li>
        <li class="item"><span>Honey Glazed Duck /w vegetable</span><span class="price">$16.90</span></li>
      </ul>
    </div>
    <div class="section">
      <h2 class="section-title">Seafood</h2>
      <ul class="items">
        <li class="item"><span>Garlic Prawn</span><span class="price">$16.90</span></li>
        <li class="item"><span>Tamarind Prawn</span><span class="price">$16.90</span></li>
        <li class="item"><span>Laab Fish</span><span class="price">$16.90</span></li>
        <li class="item"><span>Crispy Fish/w Sweet Chilli Salsa</span><span class="price">$16.90</span></li>
        <li class="item"><span>Chilli&amp;Lime Calamari Salad</span><span class="price">$16.90</span></li>
        <li class="item"><span>Salt &amp; Pepper Calamari</span><span class="price">$16.90</span></li>
        <li class="item"><span>Spicy Seafood</span><span class="price">$16.90</span></li>
        <li class="item"><span>Crispy Barramundi/w Green Mango Salad (Seasonal)</span><span class="price">$22.90</span></li>
        <li class="item"><span>Soft shell Chilli Crab</span><span class="price">$22.90</span></li>
      </ul>
    </div>
    <div class="footer-band">
      <span></span>
      <div class="badge badge-plain" aria-label="Gluten free options badge"></div>
    </div>
  </section>

  <section class="panel">
    <div class="section">
      <h2 class="section-title">Noodle</h2>
      <ul class="items">
        <li class="item"><span>Pad Thai</span><span class="price">$12.50</span></li>
        <li class="item"><span>Pad Thai Prawn</span><span class="price">$16.90</span></li>
        <li class="item"><span>Drunken Noodle</span><span class="price">$12.50</span></li>
        <li class="item"><span>Pad See Eew</span><span class="price">$12.50</span></li>
        <li class="item"><span>Beef Noodle Soup</span><span class="price">$12.50</span></li>
        <li class="item"><span>Seafood Laksa</span><span class="price">$16.90</span></li>
      </ul>
    </div>
    <div class="section">
      <h2 class="section-title">Rice</h2>
      <ul class="items">
        <li class="item"><span>Rice (S)</span><span class="price">$2.50</span></li>
        <li class="item"><span>Rice (L)</span><span class="price">$3.50</span></li>
        <li class="item"><span>Coconut Rice (S)</span><span class="price">$4.50</span></li>
        <li class="item"><span>Coconut Rice (L)</span><span class="price">$5.50</span></li>
        <li class="item"><span>Fried Rice</span><span class="price">$10.50</span></li>
        <li class="item"><span>Roti Bread</span><span class="price">$3.50</span></li>
      </ul>
    </div>
    <div class="section">
      <h2 class="section-title">Dessert</h2>
      <ul class="items">
        <li class="item"><span>Black Sticky Rice/w Coconut Cream</span><span class="price">$4.50</span></li>
        <li class="item"><span>Tapioca Pudding/w Lychee</span><span class="price">$4.50</span></li>
      </ul>
    </div>
    <div class="section">
      <h2 class="section-title">Drink</h2>
      <ul class="items">
        <li class="item"><span>Kola, Diet Kola, Fizzo, Lymo, Zesto -375ml</span><span class="price">$2.00</span></li>
        <li class="item"><span>Kola, Fizzo, Lymo 1.25ml</span><span class="price">$4.50</span></li>
        <li class="item"><span>Orange Juice, Apple Juice</span><span class="price">$3.50</span></li>
        <li class="item"><span>Ginger Beer</span><span class="price">$3.50</span></li>
      </ul>
    </div>
    <div class="footer-band">
      <p class="note">Free delivery within 5km<br>Minimum order</p>
      <div class="badge"><span class="badge-amount">$40</span></div>
    </div>
  </section>

</main>
</body>
</html>
```